VORN Paradigm. the way you communicate in every situation and in all environments.

I would like you to create a diagram depicting a very specific process of communication. it must follow the look of the diagram that i have attached. this is going to be used in a book called LANTERN. it is going to explain the fact that we communicate all the same way using this process as we communicate. it starts with the fact that everyone takes everything that is said personally and then moves on to filters, which is your own agenda or experience kicking in. then you move to your why it matters, which is your motivation and ends with the choice of words you use when you communicate. if you are going to be successful then you must separate the person from the issue.

Target Market(s)

market is executive business people around the world

Industry/Entity Type

Consulting

Font styles to use
Sans Serif

Colors

Designer to choose only greyscale colors for use in the design.

Requirements
Must have
• I would like it to have a diving/ocean/snorkel feel to it. The analogy we are using is to make a deep dive when you are communicating. it must have every part of the diagram you see, it starts at the top with the vorn paradigm (and the words) it then connects to the filters which connects to the why it matters with connects to the words and then end with the separating the person from the issue.
Nice to have
• we are writing a black and white book NO color. therefore the words should be clear and easy to read. Each section should be able to stand on its own so we can write about it separately.
Should not have
• the diagram DOES NOT have to look like the one i gave you. it must explain the fact that it starts with VORN and ends with Separate and must pass through the three areas to get to the SEPARATE.

```html
<!DOCTYPE html>
<html lang="en">
<head>
<meta charset="utf-8">
<title>VORN Paradigm – Communication Process</title>
<link rel="stylesheet" href="https://fonts.googleapis.com/css2?family=Roboto+Condensed:wght@400;700&display=swap">
<style>
  :root {
    --bg: #ffffff;
    --ring-dark: #9a9a9a;
    --ring-light: #cccccc;
    --dot-dark: #999999;
    --dot-light: #cdcdcd;
    --ink: #1a1a1a;
    --box-edge-strong: #2a2a2a;
    --box-edge-soft: #c4c4c4;
    --face-top: #ffffff;
    --face-bottom: #e4e4e4;
    --dash: #6e6e6e;
  }
  html, body {
    margin: 0;
    padding: 0;
    width: 1200px;
    height: 1199px;
    overflow: hidden;
    background: var(--bg);
  }
  .canvas {
    position: relative;
    width: 1080px;
    height: 1080px;
    transform: scale(1.1111, 1.1102);
    transform-origin: 0 0;
    font-family: "Roboto Condensed", "Arial Narrow", sans-serif;
    color: var(--ink);
  }
  .connectors {
    position: absolute;
    inset: 0;
  }
  .step-circle {
    position: absolute;
    width: 124px;
    height: 124px;
    margin: -62px 0 0 -62px;
    border-radius: 50%;
    background: linear-gradient(160deg, var(--face-top) 30%, var(--face-bottom));
    border: 2px solid #ffffff;
    box-sizing: border-box;
    box-shadow: 0 3px 10px rgba(0,0,0,0.35);
    display: flex;
    align-items: center;
    justify-content: center;
    text-align: center;
    font-weight: 700;
    font-size: 21px;
    line-height: 1.3;
  }
  .brand-mark { text-decoration: underline; text-underline-offset: 2px; }
  .step-note {
    position: absolute;
    width: 172px;
    height: 108px;
    box-sizing: border-box;
    border-radius: 11px;
    background: linear-gradient(200deg, var(--face-top) 40%, var(--face-bottom));
    box-shadow: 0 3px 9px rgba(0,0,0,0.22);
    display: flex;
    flex-direction: column;
    align-items: center;
    justify-content: center;
    text-align: center;
    font-size: 18px;
    line-height: 1.4;
    padding: 0 10px;
  }
  .step-note--key {
    border: 1.2px solid var(--box-edge-strong);
    font-weight: 700;
  }
  .step-note--soft { border: 1px solid var(--box-edge-soft); }
  .step-note small { font-size: 12px; line-height: 1.2; }
</style>
</head>
<body>
<main class="canvas">
  <svg class="connectors" width="1080" height="1080" viewBox="0 0 1080 1080" aria-hidden="true">
    <!-- rings -->
    <path d="M172 380 A83 83 0 0 1 338 380 L318 380 A63 63 0 0 0 192 380 Z" fill="var(--ring-dark)"/>
    <path d="M315 380 A82 82 0 0 0 479 380 L459 380 A62 62 0 0 1 335 380 Z" fill="var(--ring-light)"/>
    <path d="M457 380 A83 83 0 0 1 623 380 L603 380 A63 63 0 0 0 477 380 Z" fill="var(--ring-light)"/>
    <path d="M601 380 A82 82 0 0 0 765 380 L745 380 A62 62 0 0 1 621 380 Z" fill="var(--ring-light)"/>
    <path d="M743 380 A83 83 0 0 1 909 380 L889 380 A63 63 0 0 0 763 380 Z" fill="var(--ring-dark)"/>
    <!-- dashed leaders -->
    <g stroke="var(--dash)" stroke-width="1" stroke-dasharray="3 3">
      <line x1="255" y1="442" x2="255" y2="646"/>
      <line x1="397" y1="462" x2="397" y2="829"/>
      <line x1="540" y1="442" x2="540" y2="696"/>
      <line x1="683" y1="462" x2="683" y2="829"/>
      <line x1="826" y1="442" x2="826" y2="646"/>
    </g>
    <!-- end dots -->
    <circle cx="255" cy="646" r="12" fill="var(--dot-dark)"/>
    <circle cx="397" cy="829" r="12" fill="var(--dot-light)"/>
    <circle cx="540" cy="696" r="12" fill="var(--dot-light)"/>
    <circle cx="683" cy="829" r="12" fill="var(--dot-light)"/>
    <circle cx="826" cy="646" r="12" fill="var(--dot-dark)"/>
  </svg>

  <div class="step-circle" style="left:255px;top:380px;"><span><span class="brand-mark">VORN</span><br>Paradigm</span></div>
  <div class="step-circle" style="left:397px;top:380px;"><span>Your<br>Filters</span></div>
  <div class="step-circle" style="left:540px;top:380px;"><span>Why<br>It Matters</span></div>
  <div class="step-circle" style="left:683px;top:380px;"><span>Your<br>Words</span></div>
  <div class="step-circle" style="left:826px;top:380px;"><span>What<br>To Do</span></div>

  <div class="step-note step-note--key" style="left:168px;top:486px;">When words are taken personally, what happens?</div>
  <div class="step-note step-note--soft" style="left:311px;top:669px;">An accumulation of your experience, knowledge and values</div>
  <div class="step-note step-note--soft" style="left:454px;top:536px;">This is your compass. It is what motivates you? what drives you.</div>
  <div class="step-note step-note--soft" style="left:597px;top:669px;"><span>This is your immediate response, verbal</span><small>or perhaps non-verbal</small></div>
  <div class="step-note step-note--key" style="left:740px;top:486px;">Separate the Person from the Issue</div>
</main>
</body>
</html>
```